TK Joinery

Cabinet maker. Kitchens. Wardrobes. Vanitys. Entertainment units

Target Market(s)

Modern contemporary.geometry. colours black, gray, charcoal and orange. Matt card gloss letters

Industry/Entity Type

Entertainment

Contact Information for Business Card

Mattias Velder 0418 295 437
mattias.velder@fernmail.test
ABN 471 9052 8316

Font styles to use
Decorative

Colors
000000

Requirements
Should not have
• Pictures

```html
<!DOCTYPE html>
<html lang="en">
<head>
<meta charset="utf-8">
<title>TK Joinery — Business Card</title>
<link rel="stylesheet" href="https://fonts.googleapis.com/css2?family=Questrial&display=swap">
<style>
  :root {
    --backdrop: #b9bbbb;
    --card-dark: #1b1b1b;
    --card-light: #f1f1f1;
    --charcoal: #4d5358;
    --grey-text: #5a5e62;
    --light-grey: #c9cbcc;
    --orange: #e8792a;
  }
  * { margin: 0; padding: 0; box-sizing: border-box; }
  html, body {
    width: 1200px; height: 1048px; overflow: hidden;
    background: var(--backdrop);
    font-family: "Questrial", "Century Gothic", sans-serif;
  }
  .canvas { position: relative; width: 1200px; height: 1048px; }
  .card {
    position: absolute; width: 700px; height: 400px;
    box-shadow: 0 10px 26px rgba(0,0,0,0.28);
  }
  .card--back { left: 400px; top: 80px; background: var(--card-dark); }
  .card--front { left: 100px; top: 560px; background: var(--card-light); }

  /* services list */
  .services { position: absolute; left: 60px; top: 58px; }
  .services__title { color: var(--orange); font-size: 22px; margin-bottom: 8px; }
  .services__list { list-style: none; }
  .services__item {
    display: flex; align-items: center; gap: 10px;
    color: var(--light-grey); font-size: 18px; line-height: 25px;
  }
  .tick { width: 16px; height: 16px; flex: none; }

  /* wordmark */
  .wordmark { position: absolute; display: flex; align-items: center; gap: 14px; }
  .wordmark__square { width: 30px; height: 30px; background: var(--orange); flex: none; }
  .wordmark__name { font-size: 26px; letter-spacing: 8px; }
  .card--back .wordmark { left: 380px; top: 200px; }
  .card--back .wordmark__name { color: var(--light-grey); }
  .card--front .wordmark { left: 60px; top: 90px; }
  .card--front .wordmark__name { color: var(--charcoal); }

  /* contact block */
  .contact { position: absolute; left: 360px; top: 210px; color: var(--grey-text); }
  .contact__name { font-size: 30px; letter-spacing: 1px; margin-bottom: 12px; }
  .contact__row { display: flex; align-items: center; gap: 10px; font-size: 20px; line-height: 32px; }
  .contact__icon { width: 20px; height: 16px; flex: none; }
</style>
</head>
<body>
<main class="canvas">

  <section class="card card--back" aria-label="Card back">
    <div class="services">
      <h2 class="services__title">Our Services</h2>
      <ul class="services__list">
        <li class="services__item"><svg class="tick" viewBox="0 0 16 16"><rect x="1" y="3" width="12" height="12" fill="none" stroke="#e8792a" stroke-width="1.5"/><path d="M3 9l3 3 8-10" fill="none" stroke="#e8792a" stroke-width="2.4"/></svg>Cabinet maker</li>
        <li class="services__item"><svg class="tick" viewBox="0 0 16 16"><rect x="1" y="3" width="12" height="12" fill="none" stroke="#e8792a" stroke-width="1.5"/><path d="M3 9l3 3 8-10" fill="none" stroke="#e8792a" stroke-width="2.4"/></svg>Kitchens</li>
        <li class="services__item"><svg class="tick" viewBox="0 0 16 16"><rect x="1" y="3" width="12" height="12" fill="none" stroke="#e8792a" stroke-width="1.5"/><path d="M3 9l3 3 8-10" fill="none" stroke="#e8792a" stroke-width="2.4"/></svg>Wardrobes</li>
        <li class="services__item"><svg class="tick" viewBox="0 0 16 16"><rect x="1" y="3" width="12" height="12" fill="none" stroke="#e8792a" stroke-width="1.5"/><path d="M3 9l3 3 8-10" fill="none" stroke="#e8792a" stroke-width="2.4"/></svg>Vanitys</li>
        <li class="services__item"><svg class="tick" viewBox="0 0 16 16"><rect x="1" y="3" width="12" height="12" fill="none" stroke="#e8792a" stroke-width="1.5"/><path d="M3 9l3 3 8-10" fill="none" stroke="#e8792a" stroke-width="2.4"/></svg>Entertainment units</li>
      </ul>
    </div>
    <div class="wordmark">
      <span class="wordmark__square"></span>
      <span class="wordmark__name">TK Joinery</span>
    </div>
  </section>

  <section class="card card--front" aria-label="Card front">
    <div class="wordmark">
      <span class="wordmark__square"></span>
      <span class="wordmark__name">TK Joinery</span>
    </div>
    <div class="contact">
      <p class="contact__name">Mattias Velder</p>
      <p class="contact__row">
        <svg class="contact__icon" viewBox="0 0 20 16"><path d="M1 6c0-3 4-4 9-4s9 1 9 4l-4 1-1-2H6L5 7z" fill="#e8792a"/><rect x="4" y="8" width="12" height="7" rx="1" fill="#e8792a"/></svg>
        0418 295 437
      </p>
      <p class="contact__row">
        <svg class="contact__icon" viewBox="0 0 20 16"><rect x="1" y="2" width="18" height="12" fill="#e8792a"/><path d="M1 2l9 7 9-7" fill="none" stroke="#f1f1f1" stroke-width="1.4"/></svg>
        mattias.velder@fernmail.test
      </p>
    </div>
  </section>

</main>
</body>
</html>
```